Postcard Design

I run a kitchen cabinet company that sells pre-manufactured cabinets, specially made by Brindlewood Cabinets. You can see their website at brindlewoodcabinets-example.com and my website at thelarchbenchco-example.com. In addition to selling cabinets I sell counter tops (laminate and granite) along with appliances.

I need a postcard design that will be targeted at new home owners who recently purchased their property and may need kitchen cabinets, counter tops and/or appliances. I do not need a list of new home owners, I will have that.

My 'shtick' is I offer FREE Delivery and FREE Installation.
When I talk to customers about pricing I routinely come in 20-30% cheaper than the big box stores.

New Home Owners - not new construction

It Company

```html
<!DOCTYPE html>
<html lang="en">
<head>
<meta charset="utf-8">
<title>The Larch Bench Co – Postcard</title>
<link rel="stylesheet" href="https://fonts.googleapis.com/css2?family=Barlow:wght@400;500;600;700&family=Barlow+Condensed:wght@500;600&display=swap">
<style>
:root{
  --page:#1b1b1b;
  --card-white:#f4f4f4;
  --card-grey:#e2e2e2;
  --panel:#4a4a4a;
  --panel-dark:#333333;
  --red:#a52a2a;
  --red-deep:#7e1c1c;
  --red-bright:#c8262a;
  --ink:#2a2a2a;
  --white:#ffffff;
  --muted:#666666;
}
*{box-sizing:border-box;margin:0;padding:0}
html,body{width:1200px;height:1200px;overflow:hidden;background:var(--page)}
body{position:relative;font-family:"Barlow",Arial,sans-serif}

.card{position:absolute;overflow:hidden;box-shadow:0 4px 14px rgba(0,0,0,.6)}

/* Back of postcard */
.card-back{left:338px;top:64px;width:764px;height:490px;
  background:linear-gradient(180deg,var(--white) 0%,var(--card-grey) 100%)}
.back-logo{position:absolute;left:10px;top:18px;font-size:21px;font-weight:600;color:var(--ink);white-space:nowrap}
.back-address{position:absolute;left:258px;top:22px;font-size:15px;color:var(--red);white-space:nowrap}
.stamp-box{position:absolute;left:643px;top:6px;width:114px;height:114px;border:1px solid #9a9a9a}
.back-photo{position:absolute;left:10px;top:61px;width:499px;height:151px;
  background:linear-gradient(90deg,#7a4a2c 0%,#b88468 45%,#e9d2c2 70%,#8a5535 100%)}
.about{position:absolute;left:10px;top:212px;width:499px;height:159px;background:var(--panel);color:var(--white);padding:22px 12px 0}
.about h2{font-size:13.5px;font-weight:700;margin-bottom:11px}
.about p{font-size:12.6px;line-height:18px;text-align:justify}
.price-banner{position:absolute;left:10px;top:371px;width:499px;height:57px;
  background:linear-gradient(180deg,var(--red-bright),var(--red-deep));
  color:var(--white);font-size:26px;padding:10px 0 0 17px;border-top:2px solid #ddd;white-space:nowrap}

/* Front of postcard */
.card-front{left:92px;top:618px;width:765px;height:480px;background:var(--panel-dark)}
.front-side{position:absolute;left:0;top:0;width:289px;height:402px;
  background:linear-gradient(180deg,#3e3e3e,#4a4a4a)}
.ribbon{position:absolute;left:10px;top:0;width:273px;height:174px}
.ribbon-text{position:absolute;left:10px;top:36px;width:273px;text-align:center;color:var(--white)}
.ribbon-text .lead{font-size:19px;display:block}
.ribbon-text .big{font-size:40px;display:block;line-height:44px}
.ribbon-text .sub{font-size:17px;display:block}
.services{position:absolute;left:14px;top:196px;list-style:none}
.services li{display:flex;align-items:center;height:31.5px;font-size:19px;color:#eeeeee;white-space:nowrap}
.services svg{width:15px;height:15px;margin-right:8px}
.front-photo{position:absolute;left:289px;top:0;width:476px;height:402px;
  background:linear-gradient(180deg,#f3f3f1 0%,#e39b5a 22%,#3a2d28 55%,#5a4a40 75%,#9a8a7a 100%)}
.front-footer{position:absolute;left:0;top:402px;width:765px;height:78px;
  background:linear-gradient(180deg,#ffffff,#e6e6e6);
  border-top:3px solid var(--red);border-bottom:3px solid var(--red)}
.front-logo{position:absolute;left:12px;top:21px;font-size:25px;font-weight:600;color:var(--ink);white-space:nowrap}
.footer-info{position:absolute;left:300px;right:12px;top:8px;text-align:center}
.offer{font-size:23px;font-weight:700;color:var(--red);white-space:nowrap;line-height:28px}
.contact{font-family:"Barlow Condensed",Arial,sans-serif;font-size:13px;color:var(--muted);white-space:nowrap;margin-top:3px}
.contact .hl{color:var(--red);font-size:16px;font-family:"Barlow Condensed",Arial,sans-serif;font-weight:500}
</style>
</head>
<body>

<section class="card card-back" aria-label="Postcard back">
  <div class="back-logo">THE LARCH BENCH CO</div>
  <div class="back-address">4820 W Tamarack Rd, Alder Falls MN 55990</div>
  <div class="stamp-box"></div>
  <div class="back-photo" role="img" aria-label="Installer fitting wooden wall cabinets in a kitchen"></div>
  <div class="about">
    <h2>About Us</h2>
    <p>Bathroom &amp; kitchen cabinets for the entire Twin Cities MN metro and the surrounding metro area - Cabinet products and cabinet installation. Get the best deal on either one with our weekly and monthly specials and price breaks on orders of kitchen or bathroom cabinets including the installation - The Twin Cities cabinets pro!</p>
  </div>
  <div class="price-banner">20-30% cheaper than the big box stores</div>
</section>

<section class="card card-front" aria-label="Postcard front">
  <div class="front-side">
    <svg class="ribbon" viewBox="0 0 273 174" preserveAspectRatio="none">
      <defs>
        <linearGradient id="ribbonFill" x1="0" y1="0" x2="0" y2="1">
          <stop offset="0" stop-color="#d42a2e"/>
          <stop offset="1" stop-color="#8e1b1d"/>
        </linearGradient>
      </defs>
      <polygon points="0,0 273,0 273,135 136,174 0,135" fill="url(#ribbonFill)"/>
      <polygon points="9,12 264,12 264,128 136,164 9,128" fill="none" stroke="#ffffff" stroke-opacity=".55" stroke-width="1"/>
    </svg>
    <div class="ribbon-text">
      <span class="lead">Your Twin Cities Choice for</span>
      <span class="big">Beautiful</span>
      <span class="sub">Cabinets/Countertops!</span>
    </div>
    <ul class="services">
      <li><svg viewBox="0 0 15 15"><rect x="1" y="1" width="13" height="13" fill="none" stroke="#c8262a" stroke-width="1.5"/><path d="M4 7.5l2.5 2.5L11 4" fill="none" stroke="#c8262a" stroke-width="1.6"/></svg>Kitchen Cabinets</li>
      <li><svg viewBox="0 0 15 15"><rect x="1" y="1" width="13" height="13" fill="none" stroke="#c8262a" stroke-width="1.5"/><path d="M4 7.5l2.5 2.5L11 4" fill="none" stroke="#c8262a" stroke-width="1.6"/></svg>Bathroom Cabinets</li>
      <li><svg viewBox="0 0 15 15"><rect x="1" y="1" width="13" height="13" fill="none" stroke="#c8262a" stroke-width="1.5"/><path d="M4 7.5l2.5 2.5L11 4" fill="none" stroke="#c8262a" stroke-width="1.6"/></svg>Countertops</li>
      <li><svg viewBox="0 0 15 15"><rect x="1" y="1" width="13" height="13" fill="none" stroke="#c8262a" stroke-width="1.5"/><path d="M4 7.5l2.5 2.5L11 4" fill="none" stroke="#c8262a" stroke-width="1.6"/></svg>Harlow Appliances</li>
      <li><svg viewBox="0 0 15 15"><rect x="1" y="1" width="13" height="13" fill="none" stroke="#c8262a" stroke-width="1.5"/><path d="M4 7.5l2.5 2.5L11 4" fill="none" stroke="#c8262a" stroke-width="1.6"/></svg>Quality Installation</li>
      <li><svg viewBox="0 0 15 15"><rect x="1" y="1" width="13" height="13" fill="none" stroke="#c8262a" stroke-width="1.5"/><path d="M4 7.5l2.5 2.5L11 4" fill="none" stroke="#c8262a" stroke-width="1.6"/></svg>Dependable Workmanship</li>
    </ul>
  </div>
  <div class="front-photo" role="img" aria-label="Kitchen with dark espresso cabinets, light countertops, orange walls and striped wood floor"></div>
  <div class="front-footer">
    <div class="front-logo">THE LARCH BENCH CO</div>
    <div class="footer-info">
      <div class="offer">FREE Delivery and FREE Installation</div>
      <div class="contact">Visit us at: <span class="hl">thelarchbenchco-example.com</span> or Call us today: <span class="hl">555-014-2290</span></div>
    </div>
  </div>
</section>

</body>
</html>
```